OLU58 biz card & Stationery

LU58 is a personalized shopping experience brought to you, that lets you find and discover fashion goods through a collection of boutiques curated by taste-makers - celebrities, stylists, designers, and fashion bloggers. Boutiques uses visual technology to help fashionistas discover and shop their look and creates the opportunity for designers to showcase their collections and latest inspirations online.

OLU58 is built on technology developed by our team of fashion experts who work with engineers to “teach” our computer systems to understand various patterns, pairings, and genre definitions. When signed into your account, OLU58 learns about your style and preferences and in turn, provides you better results and recommendations over time. Ultimately, OLU58 will provide shoppers with a much richer and interactive shopping experience and help drive traffic to retailers' websites.

We need a definitely cool business card. The card must be black! And must use our official logo which can be download from OLU58.com

The address for Letter head and evenlop, please use 4872 Crestwick Parkway, Sutie 510 Los Angeles CA90412, email will be anyone@OLU58.com, website is www.OLU58.com

thanks

We received some of the design, thanks. But most of the design are not what we want. We need a very clean version with black ground, you may also use some dark gray to add the element. please take a look at http://morvalstudio.no/work/#pelter__ostrama/, we do like this kind of design very much. hope it help.

```html
<!DOCTYPE html>
<html lang="en">
<head>
<meta charset="utf-8">
<title>OLU58 Business Card &amp; Stationery</title>
<link rel="stylesheet" href="https://fonts.googleapis.com/css2?family=Questrial&family=Arimo:ital,wght@0,400;0,700;1,700&display=swap">
<style>
  :root {
    --paper: #ffffff;
    --ink: #111111;
    --card-black: #2a2b2b;
    --mid-grey: #b5b5b5;
    --soft-grey: #d9d9d9;
    --shadow: rgba(0,0,0,0.55);
  }
  * { box-sizing: border-box; margin: 0; padding: 0; }
  html, body { width: 883px; height: 1200px; overflow: hidden; background: var(--paper); }
  .sheet { position: relative; width: 883px; height: 1200px; font-family: "Arimo", Arial, sans-serif; color: var(--ink); }

  .wordmark { font-family: "Questrial", "Helvetica Neue", sans-serif; font-weight: 400; letter-spacing: 0.5px; line-height: 1; }

  /* Letterhead */
  .letterhead {
    position: absolute; left: 101px; top: 83px; width: 696px; height: 990px;
    background: var(--paper); border: 2px solid var(--ink);
    box-shadow: 4px 4px 6px var(--shadow);
  }
  .letterhead-header { position: absolute; top: 42px; left: 0; width: 100%; text-align: center; }
  .letterhead-header .wordmark { font-size: 38px; }
  .letterhead-header .tagline { font-size: 9px; font-weight: 700; letter-spacing: 0.3px; margin-top: 2px; }
  .letterhead-header .address { font-size: 9px; font-weight: 700; margin-top: 12px; }
  .letterhead-header .email { font-size: 11px; font-weight: 700; font-style: italic; margin-top: 5px; }

  .letterhead-footer { position: absolute; left: 4px; bottom: 8px; width: 100%; }
  .letterhead-footer .wordmark { position: absolute; left: 0; bottom: 0; font-size: 84px; color: var(--mid-grey); }
  .letterhead-footer .mark-square { position: absolute; left: 252px; bottom: 64px; width: 12px; height: 12px; background: var(--soft-grey); }
  .letterhead-footer .web { position: absolute; left: 277px; bottom: 16px; font-size: 13px; font-weight: 700; }

  /* Business cards */
  .card {
    position: absolute; background: var(--card-black); color: #fff; overflow: hidden;
    box-shadow: 5px 6px 6px var(--shadow);
  }
  .card-front { left: 452px; top: 322px; width: 297px; height: 170px; transform: rotate(-9deg); }
  .card-front .wordmark { position: absolute; left: 66px; top: 66px; font-size: 33px; }
  .card-front .tagline { position: absolute; left: 66px; top: 102px; font-size: 7px; font-weight: 700; letter-spacing: 0.4px; }
  .card-front .figure {
    position: absolute; right: 0; top: 0; width: 96px; height: 100%;
    background: linear-gradient(180deg, #ffffff 0%, #efefef 100%);
    border-radius: 60px 0 0 20px;
  }

  .card-back { left: 158px; top: 415px; width: 283px; height: 166px; transform: rotate(-12deg); }
  .card-back .web { position: absolute; left: 98px; top: 70px; font-size: 9px; font-weight: 700; }
  .card-back .web-dot { position: absolute; left: 178px; top: 72px; width: 9px; height: 9px; border: 1px solid #888; border-radius: 50%; }
  .card-back .wordmark-vertical {
    position: absolute; right: 2px; top: 4px; writing-mode: vertical-rl;
    font-size: 44px; color: #fff;
  }
  .card-back .contact { position: absolute; left: 10px; bottom: 10px; font-size: 8px; font-weight: 700; line-height: 14px; }
  .card-back .contact-row { display: flex; align-items: center; gap: 5px; }
  .card-back .contact-row svg { width: 9px; height: 9px; }

  /* Envelope */
  .envelope { position: absolute; left: 55px; top: 672px; width: 497px; height: 239px; }
  .envelope-shape { position: absolute; inset: 0; }
  .envelope-brand { position: absolute; left: 32px; top: 28px; }
  .envelope-brand .wordmark { font-size: 29px; }
  .envelope-brand .tagline { font-size: 6px; font-weight: 700; letter-spacing: 0.3px; margin-top: 2px; }
  .envelope-contact { position: absolute; left: 124px; top: 41px; }
  .envelope-contact .web { font-size: 8px; font-weight: 700; }
  .envelope-contact .address { font-size: 5px; font-weight: 700; margin-top: 2px; }
  .stamp-box { position: absolute; left: 381px; top: 25px; width: 47px; height: 48px; border: 1.5px solid var(--ink); }
  .address-window { position: absolute; left: 25px; top: 112px; width: 295px; height: 74px; border: 1.5px solid var(--ink); border-radius: 7px; }
</style>
</head>
<body>
<div class="sheet">

  <section class="letterhead">
    <header class="letterhead-header">
      <div class="wordmark">OLU58</div>
      <div class="tagline">SOCIAL FASHION ONLINE</div>
      <div class="address">4872 Crestwick Parkway, Sutie 510 Los Angeles CA90412</div>
      <div class="email">Email : anyone@OLU58.com</div>
    </header>
    <footer class="letterhead-footer">
      <div class="wordmark">OLU58</div>
      <div class="mark-square"></div>
      <div class="web">WWW.OLU58.COM</div>
    </footer>
  </section>

  <div class="card card-back">
    <div class="web">www.OLU58.com</div>
    <div class="web-dot"></div>
    <div class="wordmark wordmark-vertical">OLU58</div>
    <div class="contact">
      <div class="contact-row">
        <svg viewBox="0 0 10 10"><rect x="0.5" y="2" width="9" height="6" fill="none" stroke="#fff"/><path d="M0.5 2 L5 5.5 L9.5 2" fill="none" stroke="#fff"/></svg>
        <span>anyone@OLU58.com</span>
      </div>
      <div class="contact-row">
        <svg viewBox="0 0 10 10"><circle cx="5" cy="5" r="4.5" fill="none" stroke="#fff"/><path d="M2.5 5 L5 2.8 L7.5 5 M3.3 4.5 V7.2 H6.7 V4.5" fill="none" stroke="#fff"/></svg>
        <span>4872 Crestwick Parkway, Sutie 510 Los Angeles CA90412</span>
      </div>
    </div>
  </div>

  <div class="card card-front">
    <div class="wordmark">OLU58</div>
    <div class="tagline">SOCIAL FASHION ONLINE</div>
    <div class="figure" role="img" aria-label="White silhouette of a fashion model"></div>
  </div>

  <div class="envelope">
    <svg class="envelope-shape" viewBox="0 0 497 239" width="497" height="239">
      <rect x="4" y="4" width="459" height="235" fill="#000" opacity="0.35"/>
      <path d="M458 1 H470 Q494 1 494 40 V190 Q494 229 470 229 H458 Z" fill="#fff" stroke="#111" stroke-width="1.5"/>
      <rect x="1" y="1" width="457" height="228" fill="#fff" stroke="#111" stroke-width="1.5"/>
    </svg>
    <div class="envelope-brand">
      <div class="wordmark">OLU58</div>
      <div class="tagline">SOCIAL FASHION ONLINE</div>
    </div>
    <div class="envelope-contact">
      <div class="web">WWW.OLU58.COM</div>
      <div class="address">4872 Crestwick Parkway, Sutie 510 Los Angeles CA90412</div>
    </div>
    <div class="stamp-box"></div>
    <div class="address-window"></div>
  </div>

</div>
</body>
</html>
```